New Website for ReBranded Company - CrewBeacon

We have a successful company and website currently but it is a little dated. We have re-branded the company from Harbor Signal Networks to CrewBeacon and have a new logo for the new name. We are looking to build a newer fresher website with the new name. I will need a concept of the home page and one inside page. You can see our current site at https://www.harborsignalnetworks.example and the new site will be https://www.crewbeacon.example .

I also really like the https://www.pathlantern.example/ website. I like ledgerkite.example website. I like the https://skillorbit.example/ website.

See the attached document for layout and some text to use. Use the pictures I attached as opposed to pictures from the old site as much as you can.

Target Market(s)

Business

Industry/Entity Type

Software Service

Number of Pages Required

2 page

Font styles to use
Sans Serif

Requirements
Must have
• Use the colors from my logo. Professional but modern. We want people to feel like our product makes their staff feel safer at work.
Should not have
• Don't use any red or orange (no stop colors).

```html
<!DOCTYPE html>
<html lang="en">
<head>
<meta charset="utf-8">
<title>CrewBeacon — Feel Confident That Your Staff is Protected</title>
<link rel="stylesheet" href="https://fonts.googleapis.com/css2?family=Mulish:wght@400;600;700;800&display=swap">
<style>
:root{
  --blue:#3a94d6;
  --blue-dark:#2f86c8;
  --blue-pale:#d6e8f6;
  --green:#7ab744;
  --green-pale:#e3eed6;
  --ink:#2b2b2b;
  --text:#555;
  --muted:#777;
  --bg-soft:#f0f4f8;
  --white:#fff;
  --line:#e4e8ec;
}
*{margin:0;padding:0;box-sizing:border-box}
html,body{width:1200px;height:3113px;overflow:hidden}
body{position:relative;font-family:"Mulish",Arial,sans-serif;color:var(--ink);background:var(--white)}
.abs{position:absolute}
a{color:inherit;text-decoration:none}
.btn{position:absolute;display:flex;align-items:center;justify-content:center;color:var(--white);font-weight:700;font-size:13px;border-radius:2px}
.btn--green{background:var(--green)}
.btn--blue{background:var(--blue)}

/* header */
.site-header{top:0;left:0;width:1200px;height:80px;background:var(--white);border-bottom:1px solid var(--line)}
.brand{display:flex;align-items:center;gap:10px}
.brand__dot{width:44px;height:44px;border-radius:50%;background:var(--blue)}
.brand__name{font-size:28px;font-weight:700;color:var(--blue)}
.nav{top:30px;font-size:14px;color:var(--ink)}
.nav--active{color:var(--green)}
.nav-underline{left:640px;top:77px;width:56px;height:3px;background:var(--blue)}

/* hero */
.hero{top:80px;left:0;width:1200px;height:480px;background:linear-gradient(100deg,#4a5249 0%,#6f7a70 30%,#8b8b86 55%,#5a5d60 80%,#3f4448 100%)}
.hero__shade{top:80px;left:0;width:1200px;height:480px;background:linear-gradient(90deg,rgba(20,25,30,.55) 0%,rgba(20,25,30,.15) 60%,rgba(20,25,30,0) 100%)}
.hero__title{left:88px;top:214px;color:var(--white);font-size:40px;font-weight:700;line-height:1}
.hero__sub{left:88px;top:258px;color:var(--white);font-size:29px;font-weight:700}
.hero__text{left:88px;top:313px;color:var(--white);font-size:19px;line-height:23px;width:360px}

/* features */
.features{top:560px;left:0;width:1200px;height:300px;background:var(--bg-soft)}
.feature{top:640px;width:300px;text-align:center}
.feature__icon{display:block;margin:0 auto 14px;width:64px;height:64px}
.feature__text{font-size:16px;line-height:19px;color:#444}
.divider-v{top:628px;width:1px;height:160px;background:#c9ced3}

/* wave */
.wave-a{top:820px;left:0;width:1200px;height:460px}
.intro__title{top:986px;left:0;width:1200px;text-align:center;font-size:31px;font-weight:700}
.intro__sub{top:1042px;left:0;width:1200px;text-align:center;font-size:19px;line-height:24px;color:var(--text)}

/* why */
.why{top:1279px;left:0;width:1200px;height:430px;background:var(--blue)}
.why__title{top:1326px;left:0;width:1200px;text-align:center;color:var(--white);font-size:31px;font-weight:700}
.why-item{top:1392px;width:340px;color:var(--white)}
.why-item__icon{position:absolute;left:0;top:2px;width:34px;height:38px}
.why-item__body{margin-left:48px}
.why-item__head{font-size:16px;font-weight:700;margin-bottom:14px}
.why-item__text{font-size:13px;line-height:19px}
.why-item__label{font-size:13px;font-weight:700;line-height:19px}
.checks{list-style:none;font-size:13px;line-height:19px;display:grid;grid-template-columns:125px 125px}
.checks li::before{content:"✓";margin-right:6px;opacity:.8}
.rule{top:1571px;height:1px;background:rgba(255,255,255,.7)}

.soft-band{top:1708px;left:0;width:1200px;height:280px;background:var(--bg-soft)}
.promo{top:1668px;width:496px;height:240px;display:flex;flex-direction:column;align-items:center;justify-content:center;color:var(--white);text-align:center}
.promo--phone{left:88px;background:linear-gradient(135deg,#4f5760,#2e3338 60%,#3c4248)}
.promo--hand{left:616px;background:linear-gradient(135deg,#2b3340,#3f4c5c 50%,#273040)}
.promo__text{font-size:16px;font-weight:700;line-height:19px}
.promo__stats{display:flex;align-items:center;gap:26px;margin-top:26px}
.promo__stat{color:var(--blue);font-size:16px;font-weight:700}
.promo__cover{font-size:10px}

/* plan */
.plan__title{top:2050px;left:0;width:1200px;text-align:center;font-size:31px;font-weight:700}
.plan-card{top:2163px;width:320px;height:214px;background:var(--white);border:1px solid #eceff2}
.plan-badge{top:2121px;width:84px;height:84px;border:5px solid var(--blue);border-radius:50%;background:var(--white);display:flex;align-items:center;justify-content:center;font-size:26px;font-weight:700;color:var(--green)}
.plan-card__head{top:2230px;font-size:16px;font-weight:700;line-height:19px;width:240px}
.plan-list{top:2260px;list-style:none;font-size:13px;line-height:19px;color:var(--text)}
.plan-list li::before{content:"✓";color:var(--blue);margin-right:7px}
.plan-card__text{top:2280px;width:210px;font-size:13px;line-height:19px;color:var(--text)}

/* cta band */
.cta{top:2440px;left:0;width:1200px;height:290px;background:linear-gradient(90deg,#7cb947 0%,#86c04f 55%,#74b13f 100%)}
.cta__wave{top:2410px;left:0;width:1200px;height:150px}
.cta__text{top:2608px;left:207px;color:var(--white);font-size:26px;font-weight:700;line-height:29px}

/* footer */
.footer{top:2729px;left:0;width:1200px;height:384px;background:var(--bg-soft)}
.footer__call{top:2860px;left:88px;font-size:18px;line-height:20px}
.footer__call strong{font-weight:700}
.footer__about{top:2915px;left:88px;width:310px;font-size:12px;line-height:19px;color:var(--text)}
.fcol{top:2816px}
.fcol__head{font-size:18px;font-weight:600;margin-bottom:16px}
.fcol ul{list-style:none;font-size:12px;line-height:22.4px;color:var(--text)}
.footer__rule{top:3045px;left:88px;width:1024px;height:1px;background:#d4d9de}
.copy{top:3069px;left:88px;font-size:12px;color:var(--text)}
.copy a{color:var(--blue)}
.social{top:3062px;width:30px;height:30px;border-radius:50%;border:1px solid var(--blue)}
.to-top{top:3028px;left:1146px;width:18px;height:22px}
</style>
</head>
<body>

<!-- header -->
<header class="abs site-header">
  <a class="abs brand" style="left:88px;top:16px" href="#"><span class="brand__dot"></span><span class="brand__name">CrewBeacon</span></a>
  <a class="abs nav nav--active" style="left:648px" href="#">Home</a>
  <a class="abs nav" style="left:709px" href="#">Buy Addons</a>
  <a class="abs nav" style="left:825px;display:flex;align-items:center;gap:6px" href="#">
    <svg width="15" height="15" viewBox="0 0 16 16" fill="none" stroke="#333" stroke-width="1.3"><circle cx="8" cy="8" r="7"/><circle cx="8" cy="6.5" r="2.5"/><path d="M3.5 13c1.2-2 2.6-3 4.5-3s3.3 1 4.5 3"/></svg>Cust Login</a>
  <a class="btn btn--blue" style="left:952px;top:24px;width:160px;height:31px" href="#">Explore Your Choices</a>
  <span class="abs nav-underline"></span>
</header>

<!-- hero -->
<div class="abs hero" role="img" aria-label="Photo of a hand reaching under a desk to press a mounted panic button"></div>
<div class="abs hero__shade"></div>
<h1 class="abs hero__title">Feel Confident</h1>
<p class="abs hero__sub">That Your Staff is Protected</p>
<p class="abs hero__text">Get a revolutionary new electronic panic button</p>
<a class="btn btn--green" style="left:88px;top:387px;width:177px;height:31px" href="#">Ready To Get Started</a>
<svg class="abs" style="left:833px;top:289px" width="60" height="60" viewBox="0 0 60 60" aria-label="Play video"><circle cx="30" cy="30" r="27" fill="none" stroke="#fff" stroke-width="4"/><path d="M23 17 L42 30 L23 43Z" fill="none" stroke="#fff" stroke-width="4" stroke-linejoin="round"/></svg>

<!-- features -->
<section class="abs features"></section>
<div class="abs feature" style="left:98px">
  <svg class="feature__icon" viewBox="0 0 64 64" fill="none" stroke-width="2.4" stroke-linejoin="round"><path d="M8 30h12v26H8z" stroke="var(--blue)"/><path d="M20 32l8-10 3-10c4 0 6 3 5 8l-2 6h14c3 0 5 3 4 5l-5 21c-1 2-2 3-4 3H20" stroke="var(--blue)"/><path d="M34 4v5M24 8l3 4M44 8l-3 4M48 16h-5" stroke="var(--green)"/></svg>
  <p class="feature__text">Problems stopped<br>before they start for any type<br>of organization</p>
</div>
<div class="abs divider-v" style="left:424px"></div>
<div class="abs feature" style="left:450px">
  <svg class="feature__icon" viewBox="0 0 64 64" fill="none" stroke-width="2.4" stroke-linejoin="round"><path d="M32 4v10" stroke="var(--blue)"/><circle cx="32" cy="18" r="3" stroke="var(--blue)"/><path d="M24 14h16l5 10v34H19V24z" stroke="var(--blue)"/><path d="M37 33c-1-2-3-3-5-3-3 0-5 2-4 4s4 2 5 3 2 5-2 6c-2 0-4-1-5-3M32 27v3M32 43v3" stroke="var(--green)"/></svg>
  <p class="feature__text">Affordable prices starting at $18<br>per month. no contracts. no<br>hidden costs.</p>
</div>
<div class="abs divider-v" style="left:776px"></div>
<div class="abs feature" style="left:802px">
  <svg class="feature__icon" style="width:84px" viewBox="0 0 84 64" fill="none" stroke-width="2.4" stroke-linejoin="round"><rect x="4" y="6" width="56" height="38" rx="2" stroke="var(--blue)"/><path d="M26 44v8h12v-8M20 54h24" stroke="var(--blue)"/><rect x="12" y="14" width="12" height="10" stroke="var(--green)"/><path d="M30 16h18M30 22h12" stroke="var(--green)"/><rect x="44" y="26" width="20" height="30" rx="2" stroke="var(--blue)" fill="#f0f4f8"/><rect x="66" y="34" width="14" height="24" rx="2" stroke="var(--blue)" fill="#f0f4f8"/></svg>
  <p class="feature__text">Alerts by computer,<br>mobile device, text, phone, email,<br>monitoring and E911</p>
</div>

<!-- intro wave -->
<svg class="abs wave-a" viewBox="0 0 1200 460" preserveAspectRatio="none">
  <rect width="1200" height="460" fill="var(--bg-soft)"/>
  <path d="M480 30 C800 20 1060 70 1200 125 L1200 190 C1060 110 800 45 480 30Z" fill="var(--blue-pale)"/>
  <path d="M0 70 C300 20 760 10 1200 165 L1200 460 L0 460Z" fill="var(--white)"/>
  <path d="M0 300 C220 370 420 420 720 432 C420 440 200 400 0 340Z" fill="var(--green-pale)"/>
  <path d="M0 345 C300 430 780 460 1200 352 L1200 460 L0 460Z" fill="var(--blue)"/>
</svg>
<h2 class="abs intro__title">Your Empoyees Shouldn’t Feel Alone When They Need Help</h2>
<p class="abs intro__sub">Does this problem make you feel frustrated and anxious?<br>put a simple solution in their hands</p>
<a class="btn btn--blue" style="left:511px;top:1117px;width:175px;height:30px" href="#">Ready To Get Started</a>

<!-- why us -->
<section class="abs why"></section>
<h2 class="abs why__title">Why Businesses Choose Us</h2>
<div class="abs why-item" style="left:88px">
  <svg class="why-item__icon" viewBox="0 0 34 38" fill="none" stroke="#fff" stroke-width="2.4"><path d="M17 2 L31 7 V18 C31 27 25 33 17 36 C9 33 3 27 3 18 V7Z"/></svg>
  <div class="why-item__body">
    <h3 class="why-item__head">Easy to use</h3>
    <p class="why-item__text">Press a button and let the right people know you need help and open a chat window letting everyone talk on resolving their problem.</p>
  </div>
</div>
<div class="abs why-item" style="left:440px">
  <svg class="why-item__icon" viewBox="0 0 34 38" fill="none" stroke="#fff" stroke-width="2.4"><path d="M4 26 V18 C4 10 10 4 17 4 S30 10 30 18 V26"/><rect x="3" y="22" width="7" height="12" rx="2"/><rect x="24" y="22" width="7" height="12" rx="2"/></svg>
  <div class="why-item__body">
    <h3 class="why-item__head">Communicate the way you want</h3>
    <p class="why-item__label">We give you lots of options:</p>
    <ul class="checks"><li>Computer</li><li>Text</li><li>Mobile</li><li>E911</li><li>Email</li><li>Call Center</li><li>Phone call</li></ul>
  </div>
</div>
<div class="abs why-item" style="left:796px">
  <svg class="why-item__icon" viewBox="0 0 34 38" fill="none" stroke="#fff" stroke-width="2.4"><path d="M17 2 V36 M24 10 C22 7 20 6 17 6 C13 6 10 8 10 12 C10 20 25 16 25 25 C25 29 21 31 17 31 C13 31 10 29 9 26"/></svg>
  <div class="why-item__body">
    <h3 class="why-item__head">Cost effective protection</h3>
    <p class="why-item__text">By leveraging your existing network and equipment we can lower your costs to give better options to your staff.</p>
  </div>
</div>
<span class="abs rule" style="left:208px;width:287px"></span>
<span class="abs rule" style="left:705px;width:287px"></span>
<a class="btn btn--green" style="left:512px;top:1557px;width:175px;height:30px" href="#">Ready To Get Started</a>

<section class="abs soft-band"></section>
<div class="abs promo promo--phone" role="img" aria-label="Dark photo of a desk telephone">
  <p class="promo__text">We know how scary it can feel to worry<br>about employee safety</p>
  <a class="btn btn--blue" style="position:static;width:144px;height:31px;margin-top:12px" href="#">Start My Demo</a>
</div>
<div class="abs promo promo--hand" role="img" aria-label="Dark photo of a hand holding a wearable alert button at a pocket">
  <p class="promo__text">That’s why we have provided a way for customers<br>to get help to staff effectively in</p>
  <div class="promo__stats"><span class="promo__stat">45 States</span><span class="promo__cover">COVERING</span><span class="promo__stat">5 Countries</span></div>
</div>

<!-- plan -->
<h2 class="abs plan__title">Simple start plan</h2>
<div class="abs plan-card" style="left:88px"></div>
<div class="abs plan-badge" style="left:135px">01</div>
<h3 class="abs plan-card__head" style="left:134px">Explore Your Choices</h3>
<ul class="abs plan-list" style="left:134px;top:2259px"><li>Pricing</li><li>Trial</li><li>Quote</li><li>Hardware</li></ul>
<div class="abs plan-card" style="left:440px"></div>
<div class="abs plan-badge" style="left:487px">02</div>
<h3 class="abs plan-card__head" style="left:486px">Get Setup</h3>
<ul class="abs plan-list" style="left:486px;top:2259px"><li>Input Your Alerts</li><li>Input Your Staff</li><li>Install Our Software</li></ul>
<div class="abs plan-card" style="left:792px"></div>
<div class="abs plan-badge" style="left:839px">03</div>
<h3 class="abs plan-card__head" style="left:838px">Feel Confident Your Staff is Protected</h3>
<p class="abs plan-card__text" style="left:839px">High Five. You just too a major step to getting rid of the anxiety and frustration th is gave you.</p>
<a class="btn btn--blue" style="left:528px;top:2410px;width:144px;height:31px" href="#">Start My Demo</a>

<!-- cta band -->
<section class="abs cta" role="img" aria-label="Green tinted photo of a desk telephone"></section>
<svg class="abs cta__wave" viewBox="0 0 1200 150" preserveAspectRatio="none">
  <path d="M0 0 H1200 V60 C820 150 420 150 0 60Z" fill="var(--white)"/>
  <path d="M0 2 C120 50 220 80 360 100 C200 100 80 80 0 58Z" fill="var(--blue-pale)"/>
</svg>
<p class="abs cta__text">Stay Connected with Staff during<br>a crisis situations</p>
<a class="btn btn--blue" style="left:847px;top:2628px;width:145px;height:30px" href="#">Start My Demo</a>

<!-- footer -->
<footer class="abs footer"></footer>
<a class="abs brand" style="left:88px;top:2792px" href="#"><span class="brand__dot"></span><span class="brand__name">CrewBeacon</span></a>
<p class="abs footer__call">Call Us<br><strong>1–800–555–0142</strong></p>
<p class="abs footer__about">When employees feel alone during a threatening situation, we give them a way to let the right resources know that they need help so you can feel confident that your staff is protected.</p>
<div class="abs fcol" style="left:495px"><h4 class="fcol__head">Shop</h4><ul><li>Add Ons</li><li>Start My Demo</li><li>Custom Quote</li><li>Start Trial</li></ul></div>
<div class="abs fcol" style="left:680px"><h4 class="fcol__head">About</h4><ul><li>Affiliates</li><li>Contact</li><li>Support</li><li>Existing Customers</li><li>Industries</li><li>Blog</li><li>FAQ</li></ul></div>
<div class="abs fcol" style="left:880px"><h4 class="fcol__head">Legal</h4><ul><li>Privacy Policy</li><li>Terms of Use</li><li>End User License Agreement</li></ul></div>
<svg class="abs to-top" viewBox="0 0 18 22" fill="none" stroke="var(--blue)" stroke-width="2"><path d="M9 2 L16 20 L9 15 L2 20Z"/></svg>
<span class="abs footer__rule"></span>
<p class="abs copy">© 2020 <a href="#">CrewBeacon</a>. All Right Reserved</p>
<span class="abs social" style="left:880px"></span>
<span class="abs social" style="left:919px;border-color:var(--green)"></span>
<span class="abs social" style="left:958px"></span>
<span class="abs social" style="left:996px"></span>

</body>
</html>
```